Craft Harbor(PowerPoint Template)
Craft Harbor
Building Teams That Lead
Business focus on 4 key areas:
1. Skills Training.
2. Leadership Training
3. Consultancy
4. Coaching
Consulting
Corporate. To be used in mainly for training purposes. Secondary use for Presentation.
I would like clean and bright background so fonts can be visible. Please be creative.
Ai file for Logo

```html
<!DOCTYPE html>
<html lang="en">
<head>
<meta charset="utf-8">
<title>Craft Harbor – Presentation Template</title>
<link href="https://fonts.googleapis.com/css2?family=Arimo:ital,wght@0,400;0,700;1,700&display=swap" rel="stylesheet">
<style>
:root{
  --canvas:#ececec;
  --slide:#ffffff;
  --red:#d7261e;
  --red-dark:#a8140f;
  --orange:#f39a1f;
  --yellow:#f6c51c;
  --blue:#1f6fc4;
  --blue-dark:#0d3f86;
  --ink:#3a3a3a;
  --muted:#8a8a8a;
  --rule:#d9d9d9;
}
*{margin:0;padding:0;box-sizing:border-box}
html,body{width:1200px;height:682px;overflow:hidden;background:var(--canvas);font-family:"Arimo",Arial,sans-serif;color:var(--ink)}
.canvas{position:relative;width:1200px;height:682px}
.slide{position:absolute;width:372px;height:283px;background:var(--slide);overflow:hidden;box-shadow:0 1px 3px rgba(0,0,0,.18)}
.c1{left:19px}.c2{left:413px}.c3{left:806px}
.r1{top:24px}.r2{top:336px}
.slide-deco{position:absolute;inset:0;width:100%;height:100%}
.brand{position:absolute;display:flex;align-items:center;gap:6px}
.brand-mark{width:14px;height:14px;background:var(--red)}
.brand-name{font-weight:700;color:var(--ink);font-size:22px;letter-spacing:-.3px;white-space:nowrap}
.brand-tag{position:absolute;font-weight:700;font-size:8px;color:var(--muted);letter-spacing:.5px;white-space:nowrap}
.heading{position:absolute;left:12px;top:10px;font-weight:700;font-style:italic;color:var(--red);font-size:13px;letter-spacing:.2px}
.heading-rule{position:absolute;left:0;right:0;top:28px;height:1px;background:var(--rule)}
.subhead{position:absolute;font-weight:700;font-style:italic;color:var(--ink);font-size:12px}
.body{position:absolute;font-size:6.5px;line-height:1.45;color:var(--muted)}
.footer-rule{position:absolute;left:12px;right:12px;bottom:16px;height:1px;background:var(--rule)}
.page-no{position:absolute;left:0;right:0;bottom:6px;text-align:center;font-size:6px;color:var(--muted)}
.footer-brand{position:absolute;right:14px;bottom:20px;display:flex;align-items:center;gap:3px}
.footer-brand .brand-mark{width:7px;height:7px}
.footer-brand .brand-name{font-size:10px}
/* title slide */
.title-band{position:absolute;left:0;right:24px;top:118px;height:62px;background:linear-gradient(180deg,#2f86dd,var(--blue-dark))}
.title-band-accent{position:absolute;right:0;top:118px;width:24px;height:62px;background:linear-gradient(180deg,var(--red),var(--red-dark))}
.title-name{position:absolute;left:14px;top:124px;color:#fff;font-weight:700;font-size:15px}
.title-sub{position:absolute;left:14px;top:142px;color:#fff;font-size:9px}
.title-note{position:absolute;left:14px;top:156px;color:#dce9f8;font-size:6px;line-height:1.4;width:230px}
/* org chart */
.org{position:absolute;left:170px;top:60px;width:192px;height:120px}
/* photo */
.photo{position:absolute;left:218px;top:44px;width:108px;height:122px;background:linear-gradient(160deg,#b9a48f,#6f5a48)}
/* chart */
.chart{position:absolute;left:12px;top:40px;width:120px;height:140px}
.groups{position:absolute;left:150px;top:40px;width:210px;display:grid;grid-template-columns:1fr 1fr;gap:8px 10px}
.group-title{font-weight:700;font-size:6.5px;color:var(--ink)}
.group-text{font-size:5.5px;line-height:1.4;color:var(--muted)}
/* closing */
.slide.closing{background:linear-gradient(135deg,#e23a2a,var(--red-dark))}
.closing .brand-name{color:#fff;font-size:30px}
.closing .brand-mark{background:#fff;width:18px;height:18px}
.closing .brand-tag{color:#fde0dc;font-size:10px}
.thanks{position:absolute;left:112px;top:176px;color:#fff;font-size:13px}
.thanks-sub{position:absolute;left:160px;top:194px;color:#fff;font-size:11px}
</style>
</head>
<body>
<main class="canvas">

  <!-- Title slide -->
  <section class="slide c1 r1">
    <svg class="slide-deco" viewBox="0 0 372 283" aria-hidden="true">
      <polygon points="200,283 290,190 372,190 372,283" fill="#f3f3f3"/>
      <polygon points="250,0 372,0 372,110 320,110" fill="#f6f6f6"/>
    </svg>
    <div class="brand" style="left:16px;top:52px"><span class="brand-mark"></span><span class="brand-name">Craft Harbor</span></div>
    <div class="brand-tag" style="left:36px;top:80px">BUILDING TEAMS THAT LEAD...</div>
    <div class="title-band"></div>
    <div class="title-band-accent"></div>
    <div class="title-name">PRESENTATION NAME</div>
    <div class="title-sub">PRESENTATION TITLE</div>
    <div class="title-note">Presenter name and date go here, with the training module and session code.</div>
  </section>

  <!-- Text slide -->
  <section class="slide c2 r1">
    <div class="heading">PRESENTATION HEADING</div>
    <div class="heading-rule"></div>
    <p class="body" style="left:12px;top:40px;width:250px">Lorem Ipsum is simply dummy text of the printing and typesetting industry. Lorem Ipsum has been the industry's standard dummy text ever since the 1500s, when an unknown printer took a galley of type and scrambled it to make a type specimen book.</p>
    <p class="body" style="left:12px;top:74px;width:250px">Lorem Ipsum is simply dummy text of the printing and typesetting industry. Lorem Ipsum has been the industry's standard dummy text ever since the 1500s, when an unknown printer.</p>
    <div class="subhead" style="left:12px;top:112px">Lorem Ipsum</div>
    <p class="body" style="left:12px;top:128px;width:250px">Lorem Ipsum is simply dummy text of the printing and typesetting industry. Lorem Ipsum has been the industry's standard dummy text ever since the 1500s, when an unknown printer took a galley of type.</p>
    <div class="footer-rule"></div>
    <div class="page-no">2</div>
  </section>

  <!-- Org chart slide -->
  <section class="slide c3 r1">
    <div class="heading">PRESENTATION HEADING</div>
    <div class="heading-rule"></div>
    <div class="subhead" style="left:12px;top:36px">Lorem Ipsum</div>
    <p class="body" style="left:12px;top:52px;width:150px">Lorem Ipsum is simply dummy text of the printing and typesetting industry. Lorem Ipsum has been the industry's standard dummy text ever since the 1500s, when an unknown printer took a galley of type and scrambled it to make a type specimen book.</p>
    <p class="body" style="left:12px;top:120px;width:150px">Lorem Ipsum is simply dummy text of the printing and typesetting industry. Lorem Ipsum has been the industry's standard dummy text ever since the 1500s, when an unknown printer took a galley of type.</p>
    <svg class="org" viewBox="0 0 192 120" aria-label="Organisation chart">
      <g stroke="#9a9a9a" stroke-width="0.8" fill="none">
        <path d="M96 22 V40 M26 40 H166 M26 40 V52 M72 40 V52 M120 40 V52 M166 40 V52 M72 66 V80 M72 80 H110 M110 80 V88"/>
      </g>
      <rect x="72" y="8" width="48" height="14" fill="var(--orange)"/>
      <rect x="6" y="52" width="40" height="14" fill="var(--blue)"/>
      <rect x="52" y="52" width="40" height="14" fill="var(--blue)"/>
      <rect x="100" y="52" width="40" height="14" fill="var(--blue)"/>
      <rect x="146" y="52" width="40" height="14" fill="var(--blue)"/>
      <rect x="90" y="88" width="40" height="14" fill="var(--blue)"/>
      <g fill="#fff" font-size="5" text-anchor="middle" font-family="Arimo,Arial,sans-serif">
        <text x="96" y="17">Director</text><text x="26" y="61">Training</text><text x="72" y="61">Leadership</text>
        <text x="120" y="61">Consultancy</text><text x="166" y="61">Coaching</text><text x="110" y="97">Team</text>
      </g>
    </svg>
    <div class="footer-brand"><span class="brand-mark"></span><span class="brand-name">Craft Harbor</span></div>
    <div class="footer-rule"></div>
    <div class="page-no">3</div>
  </section>

  <!-- Photo slide -->
  <section class="slide c1 r2">
    <div class="heading">PRESENTATION HEADING</div>
    <div class="heading-rule"></div>
    <div class="subhead" style="left:12px;top:40px">Lorem Ipsum</div>
    <p class="body" style="left:12px;top:56px;width:190px">Lorem Ipsum is simply dummy text of the printing and typesetting industry. Lorem Ipsum has been the industry's standard dummy text ever since the 1500s, when an unknown printer took a galley of type.</p>
    <p class="body" style="left:12px;top:96px;width:190px">Lorem Ipsum is simply dummy text of the printing and typesetting industry. Lorem Ipsum has been the industry's standard dummy text ever since the 1500s, when an unknown printer took a galley of type and scrambled it to make a type specimen book. Lorem Ipsum is simply dummy text.</p>
    <p class="body" style="left:12px;top:154px;width:190px">Lorem Ipsum is simply dummy text of the printing and typesetting industry. Lorem Ipsum has been the industry's standard dummy text ever since the 1500s.</p>
    <div class="photo" role="img" aria-label="Photograph of a presenter"></div>
    <div class="footer-brand" style="left:14px;right:auto"><span class="brand-mark"></span><span class="brand-name">Craft Harbor</span></div>
    <div class="footer-rule"></div>
    <div class="page-no">4</div>
  </section>

  <!-- Chart slide -->
  <section class="slide c2 r2">
    <div class="heading">PRESENTATION HEADING</div>
    <div class="heading-rule"></div>
    <svg class="chart" viewBox="0 0 120 140" aria-label="Bar chart">
      <g stroke="#d0d0d0" stroke-width="0.5">
        <line x1="10" y1="20" x2="115" y2="20"/><line x1="10" y1="50" x2="115" y2="50"/>
        <line x1="10" y1="80" x2="115" y2="80"/><line x1="10" y1="110" x2="115" y2="110"/>
      </g>
      <line x1="10" y1="10" x2="10" y2="120" stroke="#999" stroke-width="0.6"/>
      <line x1="10" y1="120" x2="115" y2="120" stroke="#999" stroke-width="0.6"/>
      <rect x="18" y="18" width="16" height="102" fill="var(--red)"/>
      <rect x="42" y="62" width="16" height="58" fill="var(--orange)"/>
      <rect x="66" y="82" width="16" height="38" fill="var(--yellow)"/>
      <rect x="90" y="90" width="16" height="30" fill="var(--blue)"/>
    </svg>
    <div class="groups">
      <div><div class="group-title">Group 1</div><div class="group-text">Lorem Ipsum is simply dummy text of the printing and typesetting industry.</div></div>
      <div><div class="group-title">Group 1</div><div class="group-text">Lorem Ipsum is simply dummy text of the printing and typesetting industry.</div></div>
      <div><div class="group-title">Group 2</div><div class="group-text">Lorem Ipsum is simply dummy text of the printing and typesetting industry.</div></div>
      <div><div class="group-title">Group 2</div><div class="group-text">Lorem Ipsum is simply dummy text of the printing and typesetting industry.</div></div>
      <div><div class="group-title">Group 3</div><div class="group-text">Lorem Ipsum is simply dummy text of the printing and typesetting industry.</div></div>
      <div><div class="group-title">Group 3</div><div class="group-text">Lorem Ipsum is simply dummy text of the printing and typesetting industry.</div></div>
    </div>
    <div class="footer-brand"><span class="brand-mark"></span><span class="brand-name">Craft Harbor</span></div>
    <div class="footer-rule"></div>
    <div class="page-no">5</div>
  </section>

  <!-- Closing slide -->
  <section class="slide c3 r2 closing">
    <svg class="slide-deco" viewBox="0 0 372 283" aria-hidden="true">
      <polygon points="180,0 372,0 372,150" fill="#ffffff" opacity=".07"/>
      <polygon points="0,220 120,283 0,283" fill="#000000" opacity=".08"/>
    </svg>
    <div class="brand" style="left:70px;top:90px"><span class="brand-mark"></span><span class="brand-name">Craft Harbor</span></div>
    <div class="brand-tag" style="left:96px;top:130px">BUILDING TEAMS THAT LEAD...</div>
    <div class="thanks">Thankyou For Your Attention</div>
    <div class="thanks-sub">Lorem Ipsum</div>
  </section>

</main>
</body>
</html>
```